Veltarum

Standard Business Card design.
Sample two-sided design uploaded. White front, Black back.
Would like white shield to be on all black background side.
Willing to look at a couple creative designs, but nothing crazy.
Preference for a classic, confident, strong design.

```html
<!DOCTYPE html>
<html lang="en">
<head>
<meta charset="utf-8">
<title>Veltarum Business Card</title>
<link href="https://fonts.googleapis.com/css2?family=Montserrat:wght@400;500;800&display=swap" rel="stylesheet">
<style>
  :root {
    --stage: #d9d9d9;
    --ink: #0b0b0b;
    --paper: #ffffff;
    --muted: #222222;
  }
  * { box-sizing: border-box; margin: 0; padding: 0; }
  html, body {
    width: 1200px; height: 900px; overflow: hidden;
    background: var(--stage);
    font-family: "Montserrat", sans-serif;
  }
  .card {
    position: absolute; left: 250px;
    width: 700px; height: 400px;
    border-radius: 26px;
  }
  .card-back { top: 40px; background: var(--ink); }
  .card-front { top: 460px; background: var(--paper); color: var(--ink); }

  .back-name {
    position: absolute; inset: 0;
    display: flex; align-items: center; justify-content: center;
    gap: 18px;
    color: var(--paper); font-weight: 800; font-size: 46px; letter-spacing: 6px;
  }
  .back-name .mark-square { width: 22px; height: 22px; background: var(--paper); }

  .contact-block { position: absolute; left: 44px; top: 40px; width: 340px; }
  .brand-name {
    font-weight: 800; font-size: 34px; letter-spacing: 4px;
    padding-bottom: 10px; border-bottom: 2px solid var(--ink);
    display: inline-block;
  }
  .person-name { margin-top: 22px; font-weight: 800; font-size: 26px; letter-spacing: 1px; }
  .person-role { font-weight: 500; font-size: 15px; letter-spacing: 1px; margin-top: 2px; }
  .address { margin-top: 20px; font-size: 17px; line-height: 1.3; }
  .details { list-style: none; margin-top: 18px; font-size: 17px; }
  .details li { display: flex; align-items: center; gap: 12px; line-height: 1.55; }
  .details svg { width: 16px; height: 16px; flex: none; }

  .front-name {
    position: absolute; right: 40px; top: 0; bottom: 0; width: 280px;
    display: flex; align-items: center; justify-content: center;
    font-weight: 800; font-size: 40px; letter-spacing: 4px; color: var(--ink);
  }
</style>
</head>
<body>
  <section class="card card-back">
    <div class="back-name"><span class="mark-square"></span>VELTARUM</div>
  </section>

  <section class="card card-front">
    <div class="contact-block">
      <div class="brand-name">VELTARUM</div>
      <div class="person-name">DORIAN HALE</div>
      <div class="person-role">MANAGER</div>
      <p class="address">482 North Orchard Lane 210<br>Your Country, MN 55120</p>
      <ul class="details">
        <li>
          <svg viewBox="0 0 16 16"><path d="M3 1.5l3 3-1.5 2a9 9 0 0 0 5 5l2-1.5 3 3-2 2C6 14.5 1.5 10 1 3z" fill="#0b0b0b"/></svg>
          (612)555-0147
        </li>
        <li>
          <svg viewBox="0 0 16 16"><rect x="4" y="1" width="8" height="14" rx="1.5" fill="none" stroke="#0b0b0b" stroke-width="1.6"/><circle cx="8" cy="12.5" r="0.9" fill="#0b0b0b"/></svg>
          (612)555-01829
        </li>
        <li>
          <svg viewBox="0 0 16 16"><rect x="1" y="3" width="14" height="10" fill="#0b0b0b"/><path d="M1 3l7 6 7-6" fill="none" stroke="#fff" stroke-width="1.3"/></svg>
          hello@veltarum.com
        </li>
        <li>
          <svg viewBox="0 0 16 16"><circle cx="8" cy="8" r="6.5" fill="none" stroke="#0b0b0b" stroke-width="1.4"/><ellipse cx="8" cy="8" rx="3" ry="6.5" fill="none" stroke="#0b0b0b" stroke-width="1.2"/><path d="M1.5 8h13" stroke="#0b0b0b" stroke-width="1.2"/></svg>
          www.veltarum.com
        </li>
      </ul>
    </div>
    <div class="front-name">VELTARUM</div>
  </section>
</body>
</html>
```